Global Expert Network Firm needs business card design

We need business card design for a new company based in Seoul, South Korea called 'Corwell Insight Partners'. We recruit industry experts covering all countries and connect our client and recruited expert by phone, face-to-face meetings and etc. We are a global expert network firm that is focused on delivering high-quality experts to our clients throughout the world. Our clients include multinational corporations, global consulting firms, private equity firms, venture capital firms, asset management companies.
We have made new logo and please find attachment.(Please use new logo)
Target Market(s)
Global Consulting Firms, Investment Firms, Private Equity Firms, Venture Capital Firms.
Industry/Entity Type
Recruitment
Contact Information for Business Card
We need two Languages (English and Korean Version).
The front is Korean and the back is English version.
[The back] [English]
Company Name: Corwell Insight Partners, Inc.
CEO Name: Daniel Park
Address: #507, Hanbit Bldg, 82 Maebongsan-ro, Dobong-gu, Seoul, 01327, Korea
Tel. +82 2 718 4052
Fax. +82 2 864 1097
Mobile. +82 10 7264 8815
Email: daniel@corwellip.com
Web: www.corwellip.com
[The front] [Korean] => Described in same order as English version.
회사명: 코웰인사이트파트너스(주)
대표이사: 박도현
주소: 서울시 도봉구 매봉산로 82 한빛빌딩 507호
Tel. 02 718 4052
Fax. 02 864 1097
Mobile. 010 7264 8815
Web: www.corwellip.com
Look and feel
Each slider illustrates characteristics of the customer's brand and the style your logo design should communicate.

```html
<!DOCTYPE html>
<html lang="en">
<head>
<meta charset="utf-8">
<title>Corwell Insight Partners – Business Cards</title>
<link rel="stylesheet" href="https://fonts.googleapis.com/css2?family=Arimo:wght@400;500&family=Noto+Sans+KR:wght@400;500&display=swap">
<style>
  :root {
    --navy: #1c2557;
    --paper: #f4f5f7;
    --ink: #1c2557;
    --canvas: #e3e4e8;
  }
  * { box-sizing: border-box; margin: 0; padding: 0; }
  html, body {
    width: 1200px; height: 1000px; overflow: hidden;
    background: var(--canvas);
    font-family: "Arimo", "Noto Sans KR", Arial, sans-serif;
    color: var(--ink);
  }
  .sheet {
    width: 1200px; height: 1000px;
    display: flex; flex-direction: column; align-items: center; justify-content: center;
    gap: 44px;
  }
  .card {
    width: 770px; height: 440px;
    background: var(--navy);
    border-radius: 26px;
    padding: 14px;
  }
  .card-face {
    position: relative;
    width: 100%; height: 100%;
    background: var(--paper);
    border-radius: 18px;
  }
  .identity {
    position: absolute; left: 44px; top: 118px;
  }
  .identity-line {
    display: flex; align-items: flex-start; gap: 8px;
  }
  .person-name {
    font-size: 29px; font-weight: 500; line-height: 1; letter-spacing: 0.5px;
    padding-right: 8px; border-right: 1.5px solid var(--ink);
  }
  .company-name {
    font-size: 17px; line-height: 1.1; max-width: 150px;
  }
  .person-title {
    margin-top: 4px; font-size: 16px;
  }
  .lang-ko .person-name { font-family: "Noto Sans KR", sans-serif; font-size: 27px; }
  .lang-ko .company-name { font-family: "Noto Sans KR", sans-serif; font-size: 19px; max-width: none; padding-top: 4px; }
  .lang-ko .person-title { font-family: "Noto Sans KR", sans-serif; }
  .brand {
    position: absolute; left: 44px; top: 210px;
    display: flex; align-items: center; gap: 16px;
  }
  .brand-square {
    width: 64px; height: 64px; background: var(--navy);
  }
  .brand-name {
    font-size: 22px; font-weight: 400; color: var(--navy);
    line-height: 1.15; max-width: 160px;
  }
  .contacts {
    position: absolute; left: 380px; top: 74px;
    display: grid; grid-template-columns: 30px 1fr;
  }
  .contact-icons {
    display: flex; flex-direction: column; align-items: center;
    padding-top: 40px; gap: 9px; padding-right: 10px;
  }
  .contact-icons svg { width: 17px; height: 17px; fill: var(--navy); }
  .contact-list {
    list-style: none;
    border-left: 1.5px solid var(--ink);
    padding-left: 14px;
    font-size: 13.5px; line-height: 1.35;
  }
  .contact-list li { margin-bottom: 12px; }
  .contact-list .address { max-width: 300px; margin-bottom: 14px; }
  .lang-ko .contact-list .address { font-family: "Noto Sans KR", sans-serif; }
</style>
</head>
<body>
<main class="sheet">

  <section class="card lang-ko" aria-label="Korean side">
    <div class="card-face">
      <div class="identity">
        <div class="identity-line">
          <span class="person-name">박도현</span>
          <span class="company-name">코웰인사이트파트너스(주)</span>
        </div>
        <p class="person-title">대표이사</p>
      </div>
      <div class="brand">
        <span class="brand-square"></span>
        <span class="brand-name">Corwell Insight Partners</span>
      </div>
      <div class="contacts">
        <div class="contact-icons">
          <svg viewBox="0 0 24 24"><path d="M12 2a7 7 0 0 0-7 7c0 5 7 13 7 13s7-8 7-13a7 7 0 0 0-7-7zm0 9.5A2.5 2.5 0 1 1 12 6.5a2.5 2.5 0 0 1 0 5z"/></svg>
          <svg viewBox="0 0 24 24"><path d="M6.6 10.8a15 15 0 0 0 6.6 6.6l2.2-2.2c.3-.3.7-.4 1-.2 1.1.4 2.3.6 3.6.6.6 0 1 .4 1 1V20c0 .6-.4 1-1 1A17 17 0 0 1 3 4c0-.6.4-1 1-1h3.5c.6 0 1 .4 1 1 0 1.3.2 2.5.6 3.6.1.3 0 .7-.2 1z"/></svg>
          <svg viewBox="0 0 24 24"><path d="M6 2h10l2 2v5H6zM3 10h18v8h-3v4H6v-4H3zm5 6v4h8v-4z"/></svg>
          <svg viewBox="0 0 24 24"><path d="M7 1h10a1 1 0 0 1 1 1v20a1 1 0 0 1-1 1H7a1 1 0 0 1-1-1V2a1 1 0 0 1 1-1zm1 3v14h8V4zm4 15.5a1 1 0 1 0 0 2 1 1 0 0 0 0-2z"/></svg>
          <svg viewBox="0 0 24 24"><path d="M2 5h20v14H2zm2 2v.5l8 5.5 8-5.5V7z"/></svg>
          <svg viewBox="0 0 24 24"><path d="M12 2a10 10 0 1 0 0 20 10 10 0 0 0 0-20zm6.9 6h-3a15 15 0 0 0-1.3-3.9A8 8 0 0 1 18.9 8zM12 4c.8 1.1 1.5 2.5 1.9 4h-3.8c.4-1.5 1.1-2.9 1.9-4zM4.3 14a8 8 0 0 1 0-4h3.4a16 16 0 0 0 0 4zm.8 2h3a15 15 0 0 0 1.3 3.9A8 8 0 0 1 5.1 16zm3-8h-3a8 8 0 0 1 4.3-3.9C8.8 5.3 8.4 6.6 8.1 8zM12 20c-.8-1.1-1.5-2.5-1.9-4h3.8c-.4 1.5-1.1 2.9-1.9 4zm2.3-6H9.7a14 14 0 0 1 0-4h4.6a14 14 0 0 1 0 4zm.3 5.9c.6-1.2 1-2.5 1.3-3.9h3a8 8 0 0 1-4.3 3.9zm1.7-5.9a16 16 0 0 0 0-4h3.4a8 8 0 0 1 0 4z"/></svg>
        </div>
        <ul class="contact-list">
          <li class="address">서울시 도봉구 매봉산로 82 한빛빌딩 507호</li>
          <li>02 718 4052</li>
          <li>02 864 1097</li>
          <li>010 7264 8815</li>
          <li>daniel@corwellip.com</li>
          <li>www.corwellip.com</li>
        </ul>
      </div>
    </div>
  </section>

  <section class="card lang-en" aria-label="English side">
    <div class="card-face">
      <div class="identity">
        <div class="identity-line">
          <span class="person-name">DANIEL PARK</span>
          <span class="company-name">Corwell Insight Partners, Inc</span>
        </div>
        <p class="person-title">CEO</p>
      </div>
      <div class="brand">
        <span class="brand-square"></span>
        <span class="brand-name">Corwell Insight Partners</span>
      </div>
      <div class="contacts">
        <div class="contact-icons">
          <svg viewBox="0 0 24 24"><path d="M12 2a7 7 0 0 0-7 7c0 5 7 13 7 13s7-8 7-13a7 7 0 0 0-7-7zm0 9.5A2.5 2.5 0 1 1 12 6.5a2.5 2.5 0 0 1 0 5z"/></svg>
          <svg viewBox="0 0 24 24"><path d="M6.6 10.8a15 15 0 0 0 6.6 6.6l2.2-2.2c.3-.3.7-.4 1-.2 1.1.4 2.3.6 3.6.6.6 0 1 .4 1 1V20c0 .6-.4 1-1 1A17 17 0 0 1 3 4c0-.6.4-1 1-1h3.5c.6 0 1 .4 1 1 0 1.3.2 2.5.6 3.6.1.3 0 .7-.2 1z"/></svg>
          <svg viewBox="0 0 24 24"><path d="M6 2h10l2 2v5H6zM3 10h18v8h-3v4H6v-4H3zm5 6v4h8v-4z"/></svg>
          <svg viewBox="0 0 24 24"><path d="M7 1h10a1 1 0 0 1 1 1v20a1 1 0 0 1-1 1H7a1 1 0 0 1-1-1V2a1 1 0 0 1 1-1zm1 3v14h8V4zm4 15.5a1 1 0 1 0 0 2 1 1 0 0 0 0-2z"/></svg>
          <svg viewBox="0 0 24 24"><path d="M2 5h20v14H2zm2 2v.5l8 5.5 8-5.5V7z"/></svg>
          <svg viewBox="0 0 24 24"><path d="M12 2a10 10 0 1 0 0 20 10 10 0 0 0 0-20zm6.9 6h-3a15 15 0 0 0-1.3-3.9A8 8 0 0 1 18.9 8zM12 4c.8 1.1 1.5 2.5 1.9 4h-3.8c.4-1.5 1.1-2.9 1.9-4zM4.3 14a8 8 0 0 1 0-4h3.4a16 16 0 0 0 0 4zm.8 2h3a15 15 0 0 0 1.3 3.9A8 8 0 0 1 5.1 16zm3-8h-3a8 8 0 0 1 4.3-3.9C8.8 5.3 8.4 6.6 8.1 8zM12 20c-.8-1.1-1.5-2.5-1.9-4h3.8c-.4 1.5-1.1 2.9-1.9 4zm2.3-6H9.7a14 14 0 0 1 0-4h4.6a14 14 0 0 1 0 4zm.3 5.9c.6-1.2 1-2.5 1.3-3.9h3a8 8 0 0 1-4.3 3.9zm1.7-5.9a16 16 0 0 0 0-4h3.4a8 8 0 0 1 0 4z"/></svg>
        </div>
        <ul class="contact-list">
          <li class="address">#507, Hanbit Bldg, 82 Maebongsan-ro, Dobong-gu, Seoul, 01327, Korea</li>
          <li>+82 2 718 4052</li>
          <li>+82 2 864 1097</li>
          <li>+82 10 7264 8815</li>
          <li>daniel@corwellip.com</li>
          <li>www.corwellip.com</li>
        </ul>
      </div>
    </div>
  </section>

</main>
</body>
</html>
```